2019 Camp Brindlecove Golf Tournament

I am looking for someone to design a flyer for our golf benefit tournament. We are a Christian camp that uses this money to help provide scholarships and improve our facilities. The flyer will need to be 8.5 x 11 inches. One side will the information and registrations page. I have included a word document that has all the information. I have also included last years flyer in case that helps. We are looking for a new design, this one has been used for several years. The other side of the flyer will be used for mailing. it will need to be folded for mailing purposes. Please be sure to design half the back side as instructed, the post office is very strict about this mail out.

Target Market(s)

Golfers and potential businesses as donors

Colors

Designer to choose colors to be used in the design.

Requirements
Must have
• Golf theme, all the information provided in word document

```html
<!DOCTYPE html>
<html lang="en">
<head>
<meta charset="utf-8">
<title>Camp Brindlecove Benefit Golf Tournament Flyer</title>
<link href="https://fonts.googleapis.com/css2?family=Oswald:wght@500;600&family=Teko:wght@500;600&family=Montserrat:ital,wght@0,400;0,500;0,600;0,700;1,400;1,500;1,600&display=swap" rel="stylesheet">
<style>
  :root {
    --bg: #b7b7b7;
    --paper: #ffffff;
    --green: #119a3c;
    --green-dark: #0b7a2d;
    --ink: #222222;
    --charcoal: #2b2b2b;
    --rule: #c9c9c9;
  }
  * { box-sizing: border-box; margin: 0; padding: 0; }
  html, body { width: 1200px; height: 1200px; overflow: hidden; background: var(--bg); }
  body { position: relative; font-family: "Montserrat", sans-serif; color: var(--ink); }

  .page {
    position: absolute; top: 252px; width: 545px; height: 703px;
    background: linear-gradient(180deg, #ffffff 0%, #f4f4f4 100%);
    overflow: hidden;
  }
  .page--front { left: 44px; }
  .page--back { left: 614px; }
  .page__footer-bar { position: absolute; left: 0; right: 0; bottom: 0; height: 5px; background: var(--green); }

  .hero { position: absolute; left: 0; top: 0; width: 545px; height: 345px; }

  .title-block { position: absolute; color: #fff; text-align: center; }
  .title-block__name { font-family: "Oswald", sans-serif; font-weight: 600; font-size: 33px; line-height: 1; letter-spacing: 0.5px; white-space: nowrap; }
  .title-block__sub {
    display: flex; align-items: center; gap: 6px; justify-content: center;
    font-style: italic; font-weight: 500; font-size: 15.5px; letter-spacing: 0.6px; margin-top: 5px; white-space: nowrap;
  }
  .title-block__sub::before, .title-block__sub::after { content: ""; width: 26px; height: 1px; background: #fff; }

  .front-title { left: 222px; top: 60px; width: 318px; }

  .info-box { position: absolute; border: 1.5px solid #fff; color: #fff; text-align: center; }
  .info-box__label {
    position: absolute; top: -8px; left: 50%; transform: translateX(-50%);
    font-size: 10.5px; font-weight: 600; letter-spacing: 0.8px; padding: 0 5px; white-space: nowrap;
    background: rgba(50,90,45,0.9);
  }
  .info-box--date { left: 230px; top: 133px; width: 91px; height: 66px; }
  .info-box--date .info-box__value { font-size: 22px; font-weight: 600; line-height: 1.05; margin-top: 11px; letter-spacing: 0.5px; }
  .info-box--location { left: 383px; top: 133px; width: 123px; height: 66px; }
  .info-box--location .info-box__value { font-size: 11.5px; font-weight: 600; line-height: 1.3; margin-top: 10px; }
  .info-box--location .info-box__value span { font-weight: 400; }

  .pricing { position: absolute; left: 20px; top: 340px; width: 520px; display: flex; }
  .pricing__item { text-align: center; border-right: 1px solid var(--rule); }
  .pricing__item:last-child { border-right: none; }
  .pricing__item:nth-child(1) { width: 175px; }
  .pricing__item:nth-child(2) { width: 150px; }
  .pricing__item:nth-child(3) { width: 180px; }
  .pricing__amount { font-family: "Teko", sans-serif; font-weight: 600; font-size: 46px; line-height: 0.95; color: var(--green); }
  .pricing__label { font-size: 13.5px; font-weight: 500; color: #333; }

  .tax-note { position: absolute; left: 0; width: 545px; top: 405px; text-align: center; font-style: italic; font-size: 8.6px; line-height: 1.3; color: #333; }
  .tax-note em { color: var(--green); font-weight: 600; }

  .format-band { position: absolute; left: 0; top: 434px; width: 545px; height: 71px; background: var(--green); color: #fff; display: flex; align-items: center; }
  .format-band__schedule { width: 214px; padding-left: 62px; border-right: 1px solid rgba(255,255,255,0.7); height: 54px; }
  .format-band__heading { font-family: "Teko", sans-serif; font-weight: 500; font-size: 22px; line-height: 0.95; letter-spacing: 0.3px; }
  .format-band__time { font-size: 12.5px; font-weight: 500; line-height: 1.35; }
  .format-band__includes { padding-left: 13px; font-size: 10.8px; line-height: 1.4; width: 300px; }
  .format-band__includes b { font-weight: 600; }

  .contact-band { position: absolute; left: 0; top: 505px; width: 545px; height: 30px; background: var(--charcoal); color: #fff; text-align: center; font-style: italic; font-size: 8.4px; line-height: 1.35; padding-top: 3px; }
  .contact-band b { font-weight: 600; }

  .entry-form { position: absolute; left: 0; top: 536px; width: 545px; }
  .entry-form__title { text-align: center; font-family: "Teko", sans-serif; font-weight: 500; font-size: 23px; color: var(--green); letter-spacing: 0.4px; margin-top: 3px; line-height: 1; }
  .entry-form__cols { display: flex; gap: 26px; padding: 0 40px; margin-top: 2px; }
  .entry-form__col { flex: 1; font-size: 9px; color: #333; }
  .entry-form__col h3 { font-size: 10.5px; font-weight: 600; color: #111; margin-bottom: 8px; white-space: nowrap; line-height: 13px; }
  .entry-form__col h3 span { margin: 0 12px; }
  .field { border-bottom: 1px solid var(--rule); height: 11px; line-height: 10.5px; position: relative; }
  .field span.st { position: absolute; left: 94px; }
  .field span.zip { position: absolute; left: 140px; }
  .checks { line-height: 13px; margin-top: 6px; }
  .box { display: inline-block; width: 8px; height: 8px; border: 1px solid var(--green); vertical-align: -1px; margin-right: 1px; }
  .checks .pad { display: inline-block; width: 35px; }

  .back-title { left: 124px; top: 92px; width: 298px; height: 82px; border: 1.5px solid #fff; padding-top: 16px; }
  .back-title .title-block__name { font-size: 31px; }
  .back-title .title-block__sub { font-size: 15px; margin-top: 5px; }

  .return-address { position: absolute; left: 34px; top: 392px; }
  .return-address__name { display: flex; align-items: center; gap: 8px; font-weight: 700; font-size: 19px; color: var(--ink); letter-spacing: 0.3px; }
  .return-address__name i { width: 14px; height: 14px; background: var(--ink); display: inline-block; }
  .return-address__lines { margin-top: 24px; margin-left: 26px; font-weight: 600; font-size: 11.5px; line-height: 1.3; color: var(--ink); }

  .indicia { position: absolute; left: 436px; top: 374px; width: 78px; height: 71px; border: 1px solid #333; font-family: Arial, sans-serif; font-size: 8.3px; line-height: 1.5; text-align: center; padding-top: 4px; color: #222; }
  .indicia b { font-weight: 700; }

  .resident { position: absolute; left: 298px; top: 496px; font-family: Arial, sans-serif; font-size: 8.8px; color: #222; }
</style>
</head>
<body>

<section class="page page--front" aria-label="Information and registration side">
  <svg class="hero" viewBox="0 0 545 345">
    <defs>
      <linearGradient id="frontPhoto" x1="0" y1="0" x2="0" y2="1">
        <stop offset="0" stop-color="#2c4a2c"/>
        <stop offset="0.5" stop-color="#3e6b35"/>
        <stop offset="1" stop-color="#6f9a4c"/>
      </linearGradient>
    </defs>
    <path role="img" aria-label="Photo of a golfer swinging on a tree-lined course with a golf bag on the grass" fill="url(#frontPhoto)" d="M0 0 H545 V240 C470 225 420 250 360 290 C300 325 220 320 140 300 C80 285 30 250 0 200 Z"/>
    <path fill="var(--charcoal)" d="M360 290 C420 250 480 250 545 270 V330 C505 290 460 275 400 285 Z"/>
    <path fill="none" stroke="var(--green)" stroke-width="7" d="M0 200 C30 250 80 285 140 300 C220 320 300 325 360 290 C420 250 480 232 545 245"/>
  </svg>

  <div class="title-block front-title">
    <div class="title-block__name">CAMP BRINDLECOVE</div>
    <div class="title-block__sub">Benefit Golf Tournament</div>
  </div>

  <div class="info-box info-box--date">
    <div class="info-box__label">DATE</div>
    <div class="info-box__value">APRIL<br>5, 2019</div>
  </div>
  <div class="info-box info-box--location">
    <div class="info-box__label">LOCATION</div>
    <div class="info-box__value">The Course At<br>Willow Bend<br><span>(Maple Ridge, AR)</span></div>
  </div>

  <div class="pricing">
    <div class="pricing__item"><div class="pricing__amount">$400</div><div class="pricing__label">Per Foursome</div></div>
    <div class="pricing__item"><div class="pricing__amount">$100</div><div class="pricing__label">Per Individual</div></div>
    <div class="pricing__item"><div class="pricing__amount">$100</div><div class="pricing__label">Hole Sponsorships</div></div>
  </div>

  <p class="tax-note"><em>Tax info:</em> Camp Brindlecove is a 501(c)3 non-profit.<br>Funds raised will be used to help provided scholarships and improve facilities.</p>

  <div class="format-band">
    <div class="format-band__schedule">
      <div class="format-band__heading">SCRAMBLE FORMAT</div>
      <div class="format-band__time">11:30 Lunch</div>
      <div class="format-band__time">12:30 Shotgun Start</div>
    </div>
    <p class="format-band__includes"><b>Includes:</b> Lunch, 18 holes, cart, hole-in-one prize, closest to the pin contest, longest drive contest, and door prizes.</p>
  </div>

  <div class="contact-band">For more information call <b>501-555-0142</b> or email <b>dana@campbrindlecove.org</b>.<br>This form is also available on our website, <b>campbrindlecove.org</b>.</div>

  <div class="entry-form">
    <h2 class="entry-form__title">CAMP BRINDLECOVE ENTRY AND SPONSORSHIP FORM</h2>
    <div class="entry-form__cols">
      <div class="entry-form__col">
        <h3>TEAM - $400<span>OR</span>INDIVIDUAL - $100</h3>
        <div class="field">Name</div>
        <div class="field">Address</div>
        <div class="field">City<span class="st">St</span><span class="zip">Zip</span></div>
        <div class="field">Phone</div>
        <div class="field">Other Team Members -</div>
        <div class="field"></div>
        <div class="checks">Carts? <span class="box"></span>Yes <span class="box"></span>No &nbsp;&nbsp;&nbsp;&nbsp;How many?<br><span class="pad"></span><span class="box"></span>Check Enclosed &nbsp;&nbsp;<span class="box"></span>Bill Me</div>
      </div>
      <div class="entry-form__col">
        <h3 style="padding-left:42px">HOLE SPONSORSHIPS - $100</h3>
        <div class="field">Name</div>
        <div class="field">Address</div>
        <div class="field">City<span class="st">St</span><span class="zip">Zip</span></div>
        <div class="field">Phone</div>
        <div class="field">Name listed on your sign</div>
        <div class="field"></div>
        <div class="checks">Please mail check to Camp Brindlecove Golf<br>PO Box 4821; Maple Ridge, AR 72999</div>
      </div>
    </div>
  </div>

  <div class="page__footer-bar"></div>
</section>

<section class="page page--back" aria-label="Mailing side">
  <svg class="hero" viewBox="0 0 545 345">
    <defs>
      <linearGradient id="backPhoto" x1="0" y1="0" x2="1" y2="1">
        <stop offset="0" stop-color="#2f5a2c"/>
        <stop offset="0.55" stop-color="#1e3a22"/>
        <stop offset="1" stop-color="#5c8f45"/>
      </linearGradient>
    </defs>
    <path role="img" aria-label="Photo of golf clubs with headcovers standing in a golf bag on the course" fill="url(#backPhoto)" d="M0 0 H545 V245 C480 230 430 250 370 285 C300 320 210 310 140 300 C80 290 25 245 0 190 Z"/>
    <path fill="var(--charcoal)" d="M370 285 C430 250 490 250 545 265 V345 C510 300 465 280 410 288 Z"/>
    <path fill="none" stroke="var(--green)" stroke-width="7" d="M0 190 C25 245 80 290 140 300 C210 310 300 320 370 285 C430 250 485 235 545 250"/>
  </svg>

  <div class="title-block back-title">
    <div class="title-block__name">CAMP BRINDLECOVE</div>
    <div class="title-block__sub">Benefit Golf Tournament</div>
  </div>

  <div class="return-address">
    <div class="return-address__name"><i></i>CAMP BRINDLECOVE</div>
    <div class="return-address__lines">PO BOX 4821<br>MAPLE RIDGE AR<br>72999</div>
  </div>

  <div class="indicia">Non Profit Org<br>U.S. Postage<br><b>PAID</b><br>Maple Ridge AR<br>Permit #58</div>

  <div class="resident">OR CURRENT RESIDENT</div>

  <div class="page__footer-bar"></div>
</section>

</body>
</html>
```